Corvalt Web design

I described what I need to the doc.
Please see the my request from the following URL.
http://marblefox204.tundo.jp/CorvaltHPdraft.pdf

Please see my request and don't suggest boring typical web.

We need the innovation and the unique suggestion from you.

The log updated the site. 

Please see and design on your mind.

Thanks
corvalt

The flag on countries are for changing language.
It must be small, all designs are big.

Seeing the logo image, the we must be cool with white/black/grey.
Most designs are colorful or for kids.

```html
<!DOCTYPE html>
<html lang="en">
<head>
<meta charset="utf-8">
<title>Corvalt</title>
<link href="https://fonts.googleapis.com/css2?family=Open+Sans:wght@300;400;600&family=Comfortaa:wght@400&family=Arimo&display=swap" rel="stylesheet">
<style>
:root{
  --black:#030508;
  --graphite:#0b1117;
  --slate:rgba(70,96,118,.42);
  --slate-soft:rgba(60,84,104,.32);
  --silver:#d9dcdf;
  --white:#ffffff;
  --paper:#efefef;
  --frame:#d4d4d4;
  --cyan:#3cc8f2;
  --title-blue:#2a8ed2;
  --ink:#1c1c1c;
  --rule:#c9c9c9;
  --btn-top:#3b9be0;
  --btn-bottom:#0a4d8f;
  --mark-top:#6f8396;
  --mark-bottom:#24384c;
}
*{margin:0;padding:0;box-sizing:border-box}
html,body{width:1200px;height:958px;overflow:hidden;background:var(--white)}
.page{position:relative;width:1200px;height:958px;font-family:"Open Sans",sans-serif}

.hero{position:absolute;left:0;top:0;width:1200px;height:580px;
  background:
    radial-gradient(ellipse 260px 140px at 300px 90px,var(--slate),transparent),
    radial-gradient(ellipse 300px 160px at 930px 120px,var(--slate-soft),transparent),
    radial-gradient(ellipse 200px 120px at 60px 200px,var(--slate-soft),transparent),
    radial-gradient(ellipse 260px 140px at 1120px 300px,var(--slate-soft),transparent),
    linear-gradient(180deg,var(--graphite) 0%,#05080c 70%,var(--black) 83%,#9c9c9c 87%,#e4e4e4 93%,var(--white) 100%);}

.logo{position:absolute;left:116px;top:56px;font-weight:600;font-size:64px;letter-spacing:3px;color:var(--silver);line-height:1}

.social{position:absolute;display:flex}
.social a{color:var(--white);text-decoration:none;font-family:"Open Sans",sans-serif}
.social .mark{display:block;background:linear-gradient(180deg,var(--mark-top),var(--mark-bottom));border-radius:6px}

.social-top{left:926px;top:46px;gap:8px}
.social-top a{width:64px;display:flex;flex-direction:column;align-items:center;gap:6px;font-size:10px;line-height:12px}
.social-top .mark{width:44px;height:44px;border-radius:8px}

.showcase{position:absolute;left:131px;top:175px;width:556px;height:367px;background:var(--frame);padding:6px}
.showcase-photo{width:100%;height:100%;background:linear-gradient(180deg,#ffffff 0%,#f6f6f6 12%,#9a9a9a 40%,#4a4a52 75%,#f2f2f2 96%,#ffffff 100%)}

.headline{position:absolute;left:714px;top:188px;font-weight:300;font-size:46px;line-height:64px;color:var(--white);letter-spacing:-.6px}

.features{position:absolute;left:756px;top:262px;list-style:none}
.features li{display:flex;align-items:center;gap:13px;height:48px;font-family:"Comfortaa",sans-serif;font-size:25px;letter-spacing:-.3px;color:var(--cyan)}
.features svg{width:22px;height:22px;flex:none}

.cta{position:absolute;left:957px;top:465px;width:152px;height:44px;border-radius:4px;border:1px solid #5bb4ee;
  background:linear-gradient(180deg,var(--btn-top),var(--btn-bottom));color:var(--white);font-size:24px;font-weight:300;
  display:flex;align-items:center;justify-content:center;box-shadow:0 18px 10px -10px rgba(0,0,0,.35)}

.cards{position:absolute;left:132px;top:606px;display:flex;gap:22px}
.card{position:relative;width:302px;height:181px;border:1px solid #dcdcdc;border-radius:3px;background:linear-gradient(180deg,var(--white),var(--paper))}
.card svg.fold{position:absolute;left:-12px;top:-12px;width:326px;height:205px;pointer-events:none}
.card h2{position:absolute;left:19px;top:12px;width:266px;font-weight:300;font-size:26px;color:var(--title-blue);border-bottom:1px solid var(--rule);line-height:34px}
.card-profile h2{left:16px;top:9px;width:270px}
.card p{position:absolute;left:18px;top:68px;width:168px;font-family:"Arimo",sans-serif;font-size:13.4px;line-height:16.8px;color:var(--ink)}
.art{position:absolute}
.art-home{left:192px;top:61px;width:100px;height:111px;border-radius:6px;background:linear-gradient(160deg,#e6cf98,#b48a4a)}
.art-service{left:191px;top:65px;width:100px;height:103px;border-radius:50%;background:radial-gradient(circle at 45% 40%,#5aa0f0,#0c3c9a)}
.art-profile{left:204px;top:68px;width:84px;height:96px;border-radius:6px;background:linear-gradient(90deg,#8a1a14,#c0342a)}

.footer{position:absolute;left:0;top:832px;width:1200px;height:126px;border-top:2px solid #1a2a3a;
  background:radial-gradient(ellipse 300px 80px at 200px 60px,var(--slate-soft),transparent),
    radial-gradient(ellipse 300px 80px at 1000px 40px,var(--slate-soft),transparent),
    linear-gradient(180deg,var(--graphite),var(--black))}
.social-foot{left:0;width:1200px;top:30px;justify-content:center;gap:12px}
.social-foot a{display:flex;align-items:center;gap:5px;font-size:10px}
.social-foot .mark{width:26px;height:26px;border-radius:5px}
.copyright{position:absolute;left:0;top:75px;width:1200px;text-align:center;font-size:12px;letter-spacing:-.2px;color:var(--white)}
</style>
</head>
<body>
<div class="page">
  <header class="hero">
    <div class="logo">CORVALT</div>
    <nav class="social social-top">
      <a href="#"><span class="mark"></span>Friendlane</a>
      <a href="#"><span class="mark"></span>Chirpwave</a>
      <a href="#"><span class="mark"></span>Worknet</a>
    </nav>
    <div class="showcase"><div class="showcase-photo" role="img" aria-label="Photo of a team of business people in suits walking forward on a white background"></div></div>
    <h1 class="headline">Lorem ipsum dolor!</h1>
    <ul class="features">
      <li><svg viewBox="0 0 22 22"><rect x="1" y="5" width="15" height="15" fill="none" stroke="#cde" stroke-width="1.5"/><path d="M4 12l4 4 11-13" fill="none" stroke="#3cc8f2" stroke-width="3"/></svg>sit amet consectetur</li>
      <li><svg viewBox="0 0 22 22"><rect x="1" y="5" width="15" height="15" fill="none" stroke="#cde" stroke-width="1.5"/><path d="M4 12l4 4 11-13" fill="none" stroke="#3cc8f2" stroke-width="3"/></svg>adipisicing lorem ipsum</li>
      <li><svg viewBox="0 0 22 22"><rect x="1" y="5" width="15" height="15" fill="none" stroke="#cde" stroke-width="1.5"/><path d="M4 12l4 4 11-13" fill="none" stroke="#3cc8f2" stroke-width="3"/></svg>dolor sit amet consectet</li>
      <li><svg viewBox="0 0 22 22"><rect x="1" y="5" width="15" height="15" fill="none" stroke="#cde" stroke-width="1.5"/><path d="M4 12l4 4 11-13" fill="none" stroke="#3cc8f2" stroke-width="3"/></svg>ur adipis icing lor</li>
    </ul>
    <a class="cta">Learn More</a>
  </header>

  <section class="cards">
    <article class="card">
      <svg class="fold" viewBox="0 0 326 205"><path d="M284 0l30 0 12 40z" fill="#e2e2e2"/><path d="M0 165l12 40 30 0z" fill="#e2e2e2"/></svg>
      <h2>About Us</h2>
      <p>Lorem ipsum dolor sit amet, consectetur adipisicing elit, sed do eiusmod tempor incididunt ut labore et dolore magna</p>
      <div class="art art-home" role="img" aria-label="Icon of a folder with a small house"></div>
    </article>
    <article class="card">
      <svg class="fold" viewBox="0 0 326 205"><path d="M284 0l30 0 12 40z" fill="#e2e2e2"/><path d="M0 165l12 40 30 0z" fill="#e2e2e2"/></svg>
      <h2>Services</h2>
      <p>Duis aute irure dolor in reprehenderit in voluptate velit esse cillum dolore eu fugiat nulla pariatur.</p>
      <div class="art art-service" role="img" aria-label="Icon of a blue globe with a wrench"></div>
    </article>
    <article class="card card-profile">
      <svg class="fold" viewBox="0 0 326 205"><path d="M284 0l30 0 12 40z" fill="#e2e2e2"/><path d="M0 165l12 40 30 0z" fill="#e2e2e2"/></svg>
      <h2>Company Profile</h2>
      <p>Excepteur sint occaecat cupidatat non proident, sunt in culpa qui officia deserunt mollit anim id est laborum.</p>
      <div class="art art-profile" role="img" aria-label="Icon of a red spiral-bound portfolio notebook"></div>
    </article>
  </section>

  <footer class="footer">
    <nav class="social social-foot">
      <a href="#"><span class="mark"></span>Friendlane</a>
      <a href="#"><span class="mark"></span>Chirpwave</a>
      <a href="#"><span class="mark"></span>Worknet</a>
    </nav>
    <p class="copyright">Copyrights @ 2011 Corvalt.com. All Rights Reserved.</p>
  </footer>
</div>
</body>
</html>
```